International E-Shop Needs a Web Design

I need a web design for a new e-shop based in UK, called Voph. This will be an international collective buying website. I would like to see designs that use the colors orange and green (similar to logo colors). However, any other ideas and your vision are also welcome. The brand image is associated with words fun, social, cool and simple. The final design should look very modern and unique. Please also take into consideration user experience.

I have attached logo design. Please ignore the black background, it would be better if you extract only the name Voph on the logo design. I have also attached one example of website design which I like (especially it's modern style, bramblenest.com) and two screenshots showing icons that visualize each category (which I want to appear in my main menu bar).

*UPDATE: There is something wrong with the system and I can't upload other 3 files (web design example and 2 examples of icons). If you could give me your e-mail, then I could send all these files to you. Anyway, what I think is a modern design can be viewed on bramblenest.com

If you have any further questions, do not hesitate to ask. Thank you in advance and I look forward to your outstanding designs!

Target Market(s)

My target customers are people both male and female in the age group of 18-45 years old, who are shopping online and are present on social media.

Industry/Entity Type

Shop

Requirements
Must have
• - "What is Voph?" Button
- Log In / Register Buttons
- Currency Sliding Menu
- Shopping Cart
- "How to Buy?" and "How to Sell?" Buttons
- Follow us on Linkpond, Quillo, Zembra+
- Like Button with a number of people who like this.
- Check-In Button
- RSS Feed
- Main Menu with categories and buttons, such as Home, Electronics, Entertainment & Leisure, Fashion, Health & Beauty, Home & Garden, Jewellery & Watches, Sports & Outdoors. I would like to see also small pictures (icons) that would symbolize each category.
- Search Bar
- Carousel Slideshow with 5 different slides. The first slide on carousel slideshow should be welcoming! Something like: "Welcome to Voph! Why to shop at Voph?" - This slide should be designed in a similar way as the website.
- Four Main Categories: Latest Bargains, Your Recently Viewed Bargains, Ending Soon Bargains, Popular Bargains
- Under Each Category should be at least 3 products
- Users will be allowed to upload their own pictures, which means that picture quality and design will be different. Some kind of frames around pictures or something else (under one style) to make pictures look similar would be very helpful.
- Each Product should show the following information: Main Photo, Name, Description (Short), Total Discount (for example 35%), Current Discount (for example 5%), Starting Price, Current Price, Time Left on Bargain: 7:1:45:30
- The final design should be delivered in Photoshop format file (PSD file).
Should not have
• The choice of colors shouldn't be aggressive. Instead it should be calm and gentle. So that the user would feel himself comfortable while browsing the website.

```html
<!DOCTYPE html>
<html lang="en">
<head>
<meta charset="utf-8">
<title>Voph – Collective Buying</title>
<link href="https://fonts.googleapis.com/css2?family=Ubuntu:wght@400;500;700&family=Ubuntu+Condensed&display=swap" rel="stylesheet">
<style>
:root{
  --orange:#f15a22;
  --orange-light:#f7941d;
  --green:#8dc63f;
  --green-dark:#6aab2a;
  --text:#333;
  --muted:#555;
  --line:#ddd;
  --frame:#e2e2e2;
  --white:#fff;
}
*{margin:0;padding:0;box-sizing:border-box}
h1,h2,h3,h4,h5{font-weight:400}
html,body{width:720px;height:1200px;overflow:hidden;background:var(--white)}
body{position:relative;font-family:"Ubuntu",sans-serif;color:var(--text);font-size:7.5px;line-height:1.45}
.abs{position:absolute}
.top-rule{left:0;top:0;width:720px;height:5px;background:var(--orange)}
.brand{left:14px;top:20px;font-size:40px;font-weight:700;color:var(--orange);letter-spacing:-1px;line-height:1}
.search{left:230px;top:35px;width:246px;height:26px;border:1px solid var(--line);border-radius:3px;background:#fafafa;font-size:8px;font-style:italic;color:#555;padding:7px 10px}
.search-go{left:447px;top:34px;width:28px;height:28px;border-radius:50%;background:var(--green)}
.account{left:496px;top:6px;width:210px;height:49px;border:1px solid var(--line);border-top:none;display:flex}
.account div{flex:1;border-left:1px solid var(--line);text-align:center;font-size:8px;color:#444;padding-top:6px}
.account div:first-child{border-left:none}
.account svg{display:block;margin:0 auto 3px}
.nav{left:6px;top:90px;width:703px;height:62px;background:linear-gradient(var(--orange-light),var(--orange));border-radius:4px 4px 0 0;display:flex}
.nav a{flex:1;color:var(--white);text-decoration:none;text-align:center;font-family:"Ubuntu Condensed",sans-serif;font-size:10.5px;border-left:1px solid #f58a55;padding-top:9px;white-space:nowrap}
.nav a:first-child{border-left:none}
.nav svg{display:block;margin:0 auto 6px;height:22px}
.page{left:8px;top:152px;width:701px;height:986px;border-left:1px solid var(--line);border-right:1px solid var(--line)}
.slide-title{left:28px;top:176px;width:300px;white-space:nowrap;font-family:"Ubuntu Condensed",sans-serif;font-size:16px;letter-spacing:-0.2px;color:#222}
.slide-copy{left:33px;top:204px;width:280px;font-size:7.4px;color:var(--muted)}
.slide-copy p{margin-bottom:6px}
.btn-what{left:33px;top:298px;width:123px;height:28px;background:var(--green);border-radius:4px;color:var(--white);font-family:"Ubuntu Condensed",sans-serif;font-size:13px;padding:5px 0 0 17px;white-space:nowrap}
.dots{left:35px;top:342px;display:flex;gap:3px}
.dots i{width:8px;height:8px;border:1px solid var(--green);display:block}
.slide-visual{left:338px;top:174px;width:354px;height:168px;background:linear-gradient(135deg,#2a2d33,#7d8ea6 55%,#c9ccd2);border-radius:6px}
.divider{left:8px;top:370px;width:701px;height:1px;background:var(--line)}
.section-title{font-family:"Ubuntu Condensed",sans-serif;font-size:13.5px;color:#222;white-space:nowrap}
.about{left:20px;top:417px;width:480px;font-size:7.4px;text-align:justify}
.about p{margin-bottom:7px}
.card{width:114px}
.card .pic{height:98px;border:3px solid var(--frame)}
.card h4{color:var(--orange);font-size:8.4px;font-weight:500;margin-top:5px}
.card p{font-size:7.2px;color:var(--muted);line-height:1.45}
.card .meta{font-size:7.4px;color:#222;line-height:1.7}
.card .meta b{color:var(--orange);font-size:10px;font-weight:500;margin-left:4px}
.side-btn{left:519px;width:191px;height:34px;border-radius:3px;color:var(--white);font-size:11.5px;padding:8px 0 0 47px}
.side-btn svg{position:absolute;left:10px;top:6px}
.buy{top:382px;background:linear-gradient(var(--orange-light),#f47920)}
.sell{top:419px;background:linear-gradient(#9ed24d,var(--green-dark))}
.cat-head{left:519px;top:458px;width:191px;height:29px;background:var(--orange);color:var(--white);font-size:11px;padding:7px 0 0 13px}
.cat-list{left:530px;top:490px;list-style:none;font-size:8.4px;color:#222}
.cat-list li{height:21px;padding-left:12px;position:relative}
.cat-list li::before{content:"›";position:absolute;left:0;color:#999}
.box{left:524px;width:182px;border:1px solid var(--line)}
.upload{top:581px;height:66px;padding:9px 9px}
.upload .field{height:17px;background:#eee;border-radius:3px;margin:5px 0 8px}
.upload .go{text-align:right;font-size:7.2px}
.likes{top:657px;height:64px;padding:7px 11px;font-size:9px}
.likes .brand-sm{position:absolute;left:12px;top:24px;font-size:18px;font-weight:700;color:var(--orange)}
.likes .count{position:absolute;left:63px;top:28px;font-size:7.4px}
.likes .like{position:absolute;left:63px;top:42px;width:37px;height:14px;background:var(--orange-light);color:var(--white);font-size:8px;text-align:center;line-height:14px;border-radius:2px}
.rss-head{left:524px;top:731px;width:183px;height:27px;border:1px solid var(--line);font-family:"Ubuntu Condensed",sans-serif;font-size:13px;padding:4px 9px}
.rss{left:530px;top:764px;width:182px;font-size:7.2px}
.rss h5{font-size:8.4px;color:#111;margin-bottom:1px}
.rss p{margin-bottom:9px}
.footer{left:6px;top:1136px;width:706px;height:64px;background:linear-gradient(var(--orange),#f26b23 60%,#f58a2a);border-radius:4px 4px 0 0;color:var(--white);font-size:8.6px}
.footer .links{position:absolute;left:17px;top:9px}
.footer .copy{position:absolute;left:17px;top:30px}
.social{position:absolute;right:38px;top:8px;display:flex;gap:4px}
.social i{width:17px;height:17px;border-radius:50%;background:var(--white);display:block}
.social i.rss-dot{background:#f7a11a;border:2px solid #fff}
</style>
</head>
<body>
<div class="abs top-rule"></div>
<div class="abs brand">Voph</div>
<div class="abs search">Enter keyword here</div>
<div class="abs search-go"></div>

<div class="abs account">
  <div><svg width="22" height="20" viewBox="0 0 22 20"><path d="M1 2h4l3 10h10l2-7H7" fill="none" stroke="#5aa02c" stroke-width="2"/><circle cx="9" cy="16" r="2" fill="#5aa02c"/><circle cx="17" cy="16" r="2" fill="#5aa02c"/></svg>Shopping Cart</div>
  <div><svg width="20" height="20" viewBox="0 0 20 20"><circle cx="9" cy="6" r="4" fill="#bbb"/><path d="M2 19c0-5 3-7 7-7s7 2 7 7z" fill="#999"/><path d="M15 12v6M12 15h6" stroke="#5aa02c" stroke-width="2"/></svg>Register User</div>
  <div><svg width="18" height="20" viewBox="0 0 18 20"><path d="M5 9V6a4 4 0 0 1 8 0v3" fill="none" stroke="#888" stroke-width="2"/><rect x="2" y="9" width="14" height="10" rx="2" fill="#e2a11c"/></svg>Member Login</div>
</div>

<nav class="abs nav">
  <a href="#"><svg width="22" height="20" viewBox="0 0 22 20"><path d="M11 1 1 10h3v9h5v-6h4v6h5v-9h3z" fill="#fff"/></svg>Home</a>
  <a href="#"><svg width="26" height="20" viewBox="0 0 26 20"><rect x="4" y="1" width="18" height="13" fill="none" stroke="#fff" stroke-width="2"/><path d="M1 17h24v2H1z" fill="#fff"/></svg>Electronics</a>
  <a href="#"><svg width="22" height="20" viewBox="0 0 22 20"><rect x="1" y="1" width="20" height="18" fill="none" stroke="#fff" stroke-width="2"/><path d="M4 16l5-6 4 4 2-2 3 4z" fill="#fff"/><circle cx="15" cy="6" r="2" fill="#fff"/></svg>Entertainment</a>
  <a href="#"><svg width="20" height="22" viewBox="0 0 20 22"><path d="M10 1c2 5 8 7 8 13a8 8 0 0 1-16 0c0-4 3-5 3-9 3 2 4 4 4 6 2-3 1-7 1-10z" fill="#fff"/></svg>Fashion</a>
  <a href="#"><svg width="22" height="22" viewBox="0 0 22 22"><circle cx="11" cy="11" r="9" fill="none" stroke="#fff" stroke-width="2.5"/><path d="M11 6v10M6 11h10" stroke="#fff" stroke-width="3"/></svg>Health &amp; Beauty</a>
  <a href="#"><svg width="22" height="22" viewBox="0 0 22 22"><circle cx="11" cy="11" r="9" fill="none" stroke="#fff" stroke-width="2.5"/><path d="M11 5v6h5" fill="none" stroke="#fff" stroke-width="2.5"/></svg>Jewllery &amp; Watches</a>
  <a href="#"><svg width="30" height="22" viewBox="0 0 30 22"><circle cx="7" cy="15" r="5.5" fill="none" stroke="#fff" stroke-width="2.5"/><circle cx="23" cy="15" r="5.5" fill="none" stroke="#fff" stroke-width="2.5"/><path d="M7 15l5-8h8l3 8M12 7l3 8" fill="none" stroke="#fff" stroke-width="2.5"/><circle cx="19" cy="3" r="2.5" fill="#fff"/></svg>Sports &amp; Outdoor</a>
</nav>

<div class="abs page"></div>

<h1 class="abs slide-title">"Welcome to Voph! Why to shop at Voph?"</h1>
<div class="abs slide-copy">
  <p>Lorem ipsum dolor sit amet, consectetuer adipiscing elit. Nam cursus. Morbi ut mi. Nullam enim leo, egestas id, condimentum at, laoreet mattis, massa.</p>
  <p>Sed eleifend nonummy diam. Praesent mauris ante, elementum et, bibendum at, posuere sit amet, nibh. Duis tincidunt lectus quis dui viverra vestibulum. Suspendisse vulputate aliquam dui. Nulla elementum dui ut augue. Aliquam vehicula mi at mauris.</p>
</div>
<div class="abs btn-what">What is Voph?" &nbsp;›</div>
<div class="abs dots"><i></i><i></i><i></i><i></i><i></i></div>
<div class="abs slide-visual" role="img" aria-label="Tablet, laptop and phone showing the shop on screen"></div>
<div class="abs divider"></div>

<h2 class="abs section-title" style="left:20px;top:391px">Little About Our Company</h2>
<div class="abs about">
  <p>Lorem ipsum dolor sit amet, consectetuer adipiscing elit. Nam cursus. Morbi ut mi. Nullam enim leo, egestas id, condimentum at, laoreet mattis, massa. Sed eleifend nonummy diam. Praesent mauris ante, elementum et, bibendum at, posuere sit amet, nibh.</p>
  <p>Duis tincidunt lectus quis dui viverra vestibulum. Suspendisse vulputate aliquam dui. Nulla elementum dui ut augue. Aliquam vehicula mi at mauris. Maecenas placerat, nisl at consequat rhoncus, sem nunc gravida justo, quis eleifend arcu velit quis lacus. Morbi magna magna, tincidunt a, mattis non, imperdiet vitae, tellus. Sed odio est, auctor ac, sollicitudin in, consequat vitae, orci. Fusce id felis. Vivamus sollicitudin metus eget eros.</p>
</div>
<h2 class="abs section-title" style="left:20px;top:512px">Featued Products</h2>

<div class="abs card" style="left:18px;top:545px"><div class="pic" role="img" aria-label="Laptop" style="background:linear-gradient(#fff,#2aa7c9 45%,#222 80%,#fff)"></div><h4>Name of Products</h4><p>Lorem ipsum dolor sit amet, consectetuer adipiscing elit.</p><div class="meta">Discount<b>55%</b><br>Price range&nbsp; $85 to $150<br>Time left&nbsp;&nbsp; 3:1:45:30</div></div>
<div class="abs card" style="left:141px;top:545px"><div class="pic" role="img" aria-label="Speaker set" style="background:linear-gradient(90deg,#fff,#f3f0e8 30%,#e8d27a 50%,#f3f0e8 70%,#fff)"></div><h4>Name of Products</h4><p>Lorem ipsum dolor sit amet, consectetuer adipiscing elit.</p><div class="meta">Discount<b>55%</b><br>Price range&nbsp; $85 to $150<br>Time left&nbsp;&nbsp; 7:1:45:30</div></div>
<div class="abs card" style="left:264px;top:545px"><div class="pic" role="img" aria-label="Stack of towels" style="background:linear-gradient(90deg,#fff 25%,#d94f8a 45%,#555 60%,#fff 75%)"></div><h4>Name of Products</h4><p>Lorem ipsum dolor sit amet, consectetuer adipiscing elit.</p><div class="meta">Discount<b>55%</b><br>Price range&nbsp; $85 to $150<br>Time left&nbsp;&nbsp; 7:5:45:30</div></div>
<div class="abs card" style="left:392px;top:545px"><div class="pic" role="img" aria-label="Food chopper" style="background:linear-gradient(90deg,#fff,#e9e9ef 35%,#d8392b 70%,#fff)"></div><h4>Name of Products</h4><p>Lorem ipsum dolor sit amet, consectetuer adipiscing elit.</p><div class="meta">Discount<b>55%</b><br>Price range&nbsp; $85 to $150<br>Time left&nbsp;&nbsp; 5:1:45:30</div></div>

<div class="abs card" style="left:18px;top:742px"><div class="pic" role="img" aria-label="Wireless headphones" style="background:radial-gradient(circle,#fff 25%,#222 45%,#fff 70%)"></div><h4>Name of Products</h4><p>Lorem ipsum dolor sit amet, consectetuer adipiscing elit.</p><div class="meta">Discount<b>55%</b><br>Price range&nbsp; $85 to $150<br>Time left&nbsp;&nbsp; 1:1:45:30</div></div>
<div class="abs card" style="left:141px;top:742px"><div class="pic" role="img" aria-label="USB flash drive" style="background:linear-gradient(135deg,#fff 25%,#8d8d8d 50%,#c8c8c8 60%,#fff 80%)"></div><h4>Name of Products</h4><p>Lorem ipsum dolor sit amet, consectetuer adipiscing elit.</p><div class="meta">Discount<b>55%</b><br>Price range&nbsp; $85 to $150<br>Time left&nbsp;&nbsp; 7:1:45:30</div></div>
<div class="abs card" style="left:264px;top:742px"><div class="pic" role="img" aria-label="Gas stove" style="background:linear-gradient(#fff 20%,#2b2b2b 40%,#555 70%,#fff)"></div><h4>Name of Products</h4><p>Lorem ipsum dolor sit amet, consectetuer adipiscing elit.</p><div class="meta">Discount<b>55%</b><br>Price range&nbsp; $85 to $150<br>Time left&nbsp;&nbsp; 2:1:45:30</div></div>
<div class="abs card" style="left:392px;top:742px"><div class="pic" role="img" aria-label="Power drill" style="background:linear-gradient(90deg,#fff,#cfd3da 35%,#23308a 75%,#1b1b3c)"></div><h4>Name of Products</h4><p>Lorem ipsum dolor sit amet, consectetuer adipiscing elit.</p><div class="meta">Discount<b>55%</b><br>Price range&nbsp; $85 to $150<br>Time left&nbsp;&nbsp; 7:1:45:30</div></div>

<div class="abs card" style="left:18px;top:941px"><div class="pic" role="img" aria-label="Pendant necklace" style="background:radial-gradient(circle at 50% 65%,#6b5a35 15%,#c79a3f 25%,#fff 50%)"></div><h4>Name of Products</h4><p>Lorem ipsum dolor sit amet, consectetuer adipiscing elit.</p><div class="meta">Discount<b>55%</b><br>Price range&nbsp; $85 to $150<br>Time left&nbsp;&nbsp; 1:1:45:30</div></div>
<div class="abs card" style="left:140px;top:941px"><div class="pic" role="img" aria-label="Toy track set" style="background:radial-gradient(circle,#f1d21e 20%,#7c5fb3 35%,#fff 60%)"></div><h4>Name of Products</h4><p>Lorem ipsum dolor sit amet, consectetuer adipiscing elit.</p><div class="meta">Discount<b>55%</b><br>Price range&nbsp; $85 to $150<br>Time left&nbsp;&nbsp; 7:1:45:30</div></div>
<div class="abs card" style="left:264px;top:941px"><div class="pic" role="img" aria-label="Digital camera" style="background:radial-gradient(circle,#333 20%,#111 45%,#fff 70%)"></div><h4>Name of Products</h4><p>Lorem ipsum dolor sit amet, consectetuer adipiscing elit.</p><div class="meta">Discount<b>55%</b><br>Price range&nbsp; $85 to $150<br>Time left&nbsp;&nbsp; 2:1:45:30</div></div>
<div class="abs card" style="left:392px;top:941px"><div class="pic" role="img" aria-label="Running shoes" style="background:linear-gradient(160deg,#fff 20%,#e8ebf2 45%,#2a3566 60%,#fff 80%)"></div><h4>Name of Products</h4><p>Lorem ipsum dolor sit amet, consectetuer adipiscing elit.</p><div class="meta">Discount<b>55%</b><br>Price range&nbsp; $85 to $150<br>Time left&nbsp;&nbsp; 7:1:45:30</div></div>

<div class="abs side-btn buy"><svg width="18" height="22" viewBox="0 0 18 22"><path d="M6 1v11l-3-2-2 2 6 9h9l1-10-7-2V1z" fill="#fff"/></svg>HOW TO BUY ?</div>
<div class="abs side-btn sell"><svg width="24" height="20" viewBox="0 0 24 20"><path d="M7 8l5-6 5 6" fill="none" stroke="#fff" stroke-width="2"/><path d="M1 8h22l-3 11H4z" fill="#fff"/></svg>HOW TO SELL?</div>
<div class="abs cat-head">Our Category</div>
<ul class="abs cat-list">
  <li>Latest Bargains</li>
  <li>Your Recently Viewed Bargains</li>
  <li>Ending Soon Bargains</li>
  <li>Popular Bargains</li>
</ul>
<div class="abs box upload"><div style="font-size:9px">Upload Now</div><div class="field"></div><div class="go">Get Upload Now &nbsp;▸</div></div>
<div class="abs box likes">How Many People Like Us<span class="brand-sm">Voph</span><span class="count">2188 people like this</span><span class="like">Like</span></div>
<div class="abs rss-head">Rss Feed</div>
<div class="abs rss">
  <h5>Tittle line goes here</h5><p>Lorem ipsum dolor sit amet, consectetuer adipiscing elit. Nam cursus. Morbi ut mi. Nullam enim leo, egestas id, condimentum at</p>
  <h5>Tittle line goes here</h5><p>auris vel lacus vitae felis vestibulum volutpat. Etiam est nunc, venenatis in, tristique eu, imperdiet ac, nisl. Cum sociis natoque penatibus et magnis dis parturient montes, nascetur ridiculus mus. In iaculis facilisis massa. Etiam eu urna. Sed porta. Suspendisse quam leo, molestie sed, luctus quis, feugiat in, pede.</p>
  <h5>Tittle line goes here</h5><p>Aliquam vehicula mi at mauris. Maecenas placerat, nisl at consequat rhoncus, sem nunc gravida justo, quis eleifend arcu velit quis lacus</p>
  <h5>Tittle line goes here</h5><p>Praesent vitae lacus. Ut velit enim, vestibulum non, fermentum nec, hendrerit quis, leo. Pellentesque rutrum malesuada neque.<br>Nunc tempus felis vitae urna. Vivamus porttitor, neque at volutpat rutrum, purus nisi eleifend libero, a tempus libero lectus feugiat felis.</p>
</div>

<footer class="abs footer">
  <div class="links">Home &nbsp;| &nbsp;Products &nbsp;| &nbsp;What We Are &nbsp;| &nbsp;Rss Feed &nbsp;| &nbsp;Special &nbsp;| &nbsp;Upload &nbsp;| &nbsp;Sitemap &nbsp;| &nbsp;Contact</div>
  <div class="copy">© 2012 Company Name &nbsp;| &nbsp;All right resreved</div>
  <div class="social"><i class="rss-dot" aria-label="RSS"></i><i aria-label="Linkpond"></i><i aria-label="Quillo"></i><i aria-label="Zembra+"></i></div>
</footer>
</body>
</html>
```